Simple but impressive brochure for Consulting Company

We need a single page (back and front) brochure to introduce our company to prospective clients. We are open to different formats, but think that a trifold or double fold may work best. (fold up style brochure or a flyer with front & back).

It should be easy to print as we will need to print it as soon as possible. 8 1/2 x 11 based format is probably best, but again, we are open to suggestions.

About the Company:

We are a consulting company comprised of US Navy fighter pilots (SKYLANCE), US Navy SEALS, and business executives, that use our knowledge and experience in high risk / high performance environments to benefit our business clients. Most of our clients are in the oil and mining sector.

We deal with drilling companies and their crews and management. We do lectures and provide on-site training and coaching.

Enclosed in the "file" section are various one page handouts with information that describes what we do and how we currently project our image to our clients.

Our website is http://www.veltmorix.example

We have photographs of worksites, fighter jets, etc. available for creative use, if the quality is deemed acceptable by you, the designer, to use. We are not opposed to stock photos if those would be preferable.

We are working on a fairly tight schedule as we have an event on 4 February 2013. So we need the design done and enough time to have the final version printed. We set this project at 5 days, but can extend it a bit as needed.

We are looking for a design that is solid, professional and gives an indication of our background in high risk environments, but does not over emphasis our military experience.

Oil field related imagery would be a nice addition. In our business, we emphasis and sell the concept of SAFE and RELIABLE operations, done by people with vast experience in the field.

We take our experience in the field and aircraft carrier operations and pass those lessons to the oil field and mining operations. (primarily oil field)

In case you need to know: we have a few different versions of our LOGO in the attached files. It consists of an orb and the word KESTRAN in "Good Times" font, slightly flattened and stretched. (you can see the logo files). We also use a Kestran AXIS(tm) logo for a specific set of programs we offer.

Note: We have more files to upload, but currently it is maxed at 5 files. They will be uploaded if more are allowed or put in a Filevat.

Thank you all for your participation.  I'm sorry I could only pick one design, as so many of you are very talented and made the choice difficult.

Target Market(s)

Our buyers are managers and executives of Meridel 400 companies. Primarily male, educated, many with engineering backgrounds.

Industry/Entity Type

Training

Requirements
Must have
• Our primary desire is to convey a sense of action and professionalism to our prospective clients. I'm not sure if we have anything compulsory required with the exception of our logo.

If there is room and it makes sense, we can include the "Service Disabled Veteran" logo. (in file section)

Nice to have
• We would like an ongoing relationship with our selected designer. We will have updated brochures and web graphics in the near future.

```html
<!DOCTYPE html>
<html lang="en">
<head>
<meta charset="utf-8">
<title>Kestran Brochure Spread</title>
<link href="https://fonts.googleapis.com/css2?family=Russo+One&family=Arimo:ital,wght@0,400;0,700;1,400&display=swap" rel="stylesheet">
<style>
  :root{
    --backdrop:#e9eaec;
    --steel:#8c8f96;
    --white:#ffffff;
    --soft:#e4e7ee;
  }
  *{box-sizing:border-box;margin:0;padding:0}
  html,body{width:1200px;height:900px;overflow:hidden;background:var(--backdrop)}
  .spread{position:absolute;left:60px;top:60px;width:1080px;height:780px}
  .spread-art{position:absolute;inset:0}
  .page{position:absolute;top:0;width:540px;height:780px;color:var(--white);font-family:"Arimo",Arial,sans-serif}
  .page-left{left:0;padding:56px 46px 0 34px}
  .page-right{left:540px;padding:34px 30px 0 30px}
  .brand{font-family:"Russo One",sans-serif;font-size:34px;line-height:1;letter-spacing:1px;margin-bottom:8px}
  .head{font-family:"Russo One",sans-serif;font-size:14.5px;letter-spacing:.6px;text-transform:uppercase;line-height:1.15;margin-bottom:3px}
  .head-lg{font-size:16px}
  .body{font-size:11.6px;line-height:1.45;color:var(--soft)}
  .body-gap{margin-top:10px}
  .block{margin-top:12px}
  .block-first{margin-top:0}
  .block-mission{margin-top:14px}
  .rblock{margin-top:18px}
  .rblock-first{margin-top:0}
  .narrow{width:330px}
  .bullets{list-style:none;font-size:12.4px;line-height:1.45;color:var(--soft)}
  .bullets li::before{content:"•"}
  .cols{display:flex;gap:40px;margin-top:4px}
  .cols .bullets{width:220px}
  sup{font-size:.55em}
</style>
</head>
<body>
<div class="spread">
  <svg class="spread-art" width="1080" height="780" viewBox="0 0 1080 780">
    <defs>
      <linearGradient id="topBand" x1="0" y1="0" x2="1" y2="0">
        <stop offset="0" stop-color="#123a7c"/>
        <stop offset="1" stop-color="#0a1f47"/>
      </linearGradient>
      <linearGradient id="skyFill" x1="0" y1="0" x2="0" y2="1">
        <stop offset="0" stop-color="#5f86c4"/>
        <stop offset="1" stop-color="#1b3f7e"/>
      </linearGradient>
      <linearGradient id="deckFill" x1="0" y1="0" x2="1" y2="1">
        <stop offset="0" stop-color="#b9c4d8"/>
        <stop offset="1" stop-color="#3d4f73"/>
      </linearGradient>
      <radialGradient id="glow" cx=".5" cy=".45" r=".6">
        <stop offset="0" stop-color="#232a3a"/>
        <stop offset="1" stop-color="#121419"/>
      </radialGradient>
    </defs>
    <path d="M40 0 H540 V780 H40 Q0 780 0 740 V40 Q0 0 40 0Z" fill="url(#glow)"/>
    <path d="M540 0 H1040 Q1080 0 1080 40 V740 Q1080 780 1040 780 H540Z" fill="url(#glow)"/>
    <path d="M40 0 H540 V30 L0 85 V40 Q0 0 40 0Z" fill="url(#topBand)"/>
    <rect x="0" y="200" width="12" height="330" fill="var(--steel)"/>
    <path d="M0 745 L540 735 V780 H40 Q0 780 0 740Z" fill="url(#skyFill)" role="img" aria-label="Photo strip of a fighter jet in flight"/>
    <path d="M880 0 H1040 Q1080 0 1080 40 V120 L930 135Z" fill="url(#deckFill)" role="img" aria-label="Photo of fighter jets parked on an aircraft carrier deck"/>
    <path d="M1080 290 L1064 320 V470 L1080 500Z" fill="var(--steel)"/>
    <path d="M540 735 L1080 690 V740 Q1080 780 1040 780 H540Z" fill="url(#skyFill)" role="img" aria-label="Photo of a fighter jet flying above the clouds"/>
    <line x1="540" y1="0" x2="540" y2="780" stroke="#000" stroke-opacity=".35" stroke-width="2"/>
  </svg>

  <section class="page page-left">
    <div class="brand">KESTRAN</div>

    <div class="block block-first">
      <h3 class="head">About Kestran</h3>
      <p class="body">Kestran is a high performance training and consulting company with high performance people. Kestran's team consists of Fighter Pilots, Navy SEALS, Special Forces, Astronauts, and veteran industry &amp; corporate leaders. We leverage the credibility, experience, expertise, and ingenuity of our team to develop solutions for our clients.</p>
    </div>

    <div class="block">
      <h3 class="head">Kestran's Mission</h3>
    </div>
    <div class="block-mission">
      <h2 class="head head-lg">Optimize safety and operational excellence in complex high-risk arenas.</h2>
    </div>

    <div class="block">
      <h3 class="head">Foundation of Excellence</h3>
      <p class="body">The Foundation of Excellence is built on vision, leadership, communication, and teamwork. Using Kestran practices, high performance companies execute toward a crystal clear strategic vision that leadership clearly communicates to frontline teams and individuals. Kestran's solutions accelerate the realization of an organization's vision.</p>
    </div>

    <div class="block">
      <h3 class="head">Engine of Excellence</h3>
      <p class="body">Kestran instills the disciplines of Planning, Briefing, Execution, and the After Action Review (AAR) that raise levels of excellence and drive continuous improvement within an organization.</p>
      <p class="body body-gap"><em>The Engine of Excellence yields consistent and predictable results. Our proprietary programs provide disciplined methodologies that create deliberate actions for achieving your organization's vision.</em></p>
    </div>

    <div class="block">
      <h3 class="head">Human Performance</h3>
      <p class="body">The human element is the most important factor for success in complex high-risk organizations. Kestran laser focuses on the strengths and weaknesses of the human component. Our solutions are built to optimize leadership, decision-making, situational awareness, communications, teamwork, and more.</p>
    </div>

    <div class="block">
      <h3 class="head">Kestran AXIS<sup>TM</sup></h3>
      <p class="body">The goal of zero incidents is the hallmark of high-performing complex high-risk organizations. Our Kestran AXIS™ family of programs builds the skill sets required for organizations and individuals to embark on a true path to excellence.</p>
    </div>
  </section>

  <section class="page page-right">
    <div class="rblock rblock-first narrow">
      <h3 class="head">The "Human Component"</h3>
      <ul class="bullets">
        <li>Is the foundation for success in high-risk / high-performance operations.</li>
        <li>Is the difference between success or failure and excellence or mediocrity.</li>
        <li>Is the most neglected performance factor in most organizations.</li>
      </ul>
    </div>

    <div class="rblock">
      <h3 class="head head-lg">Kestran AXIS<sup>TM</sup> Program</h3>
      <ul class="bullets">
        <li>Laser focuses on the "Human Component".</li>
        <li>Builds a foundation for incident free operations.</li>
        <li>Three themed levels of training geared to enhance skills, disciplines, behaviors, and knowledge for operating in high-risk arenas.</li>
        <li>Tailored to each client's operational and organizational needs.</li>
        <li>Focuses on the "non-technical skills" applied by leaders, teams and individuals.</li>
      </ul>
    </div>

    <div class="rblock">
      <h3 class="head head-lg">Develops the Foundational Skills</h3>
      <div class="cols">
        <ul class="bullets"><li>Planning</li><li>Briefing</li><li>Execution</li></ul>
        <ul class="bullets"><li>After Action Review</li><li>Continuous Improvement</li></ul>
      </div>
    </div>

    <div class="rblock">
      <h3 class="head head-lg">Develops the 7 Critical Behaviors of<br>High Performing Teams</h3>
      <div class="cols">
        <ul class="bullets"><li>Leadership</li><li>Assertiveness</li><li>Communications</li></ul>
        <ul class="bullets"><li>Mission Analysis</li><li>Situational Awareness</li><li>Adaptability and Flexibility</li><li>Decision Making</li></ul>
      </div>
    </div>

    <div class="rblock">
      <h3 class="head head-lg">Explores Human Performance<br>Enhancers and Detractors</h3>
      <div class="cols">
        <ul class="bullets"><li>Threat and Error Management</li><li>Operational Risk Management</li><li>Teaching and Learning</li><li>Critical Thinking</li><li>Public Speaking Skills</li></ul>
        <ul class="bullets"><li>Workload Management</li><li>Fatigue</li><li>Stress</li><li>Judgment</li><li>And more…</li></ul>
      </div>
    </div>
  </section>
</div>
</body>
</html>
```